Dog Grass Website

We need a two page website for our new product that will be shipped to customers of a tray with grass inside for a pet to relieve themselves. We are hoping for a clean look that translates a positive and upscale message.

The first page will be informative about the product and the second page will be 'about us'.

For more information please download the files. We have attached a screenshot of what the product box will look like

```html
<!DOCTYPE html>
<html lang="en">
<head>
<meta charset="utf-8">
<title>Turf Tails — From our farm to your home</title>
<link href="https://fonts.googleapis.com/css2?family=Poppins:wght@400;500;600&family=Alice&family=Kaushan+Script&display=swap" rel="stylesheet">
<style>
:root{
  --brown:#5a2410;
  --brown-dark:#3e1708;
  --green:#6ab43e;
  --green-dark:#3f8a1f;
  --blush:#fdf2ee;
  --text:#4a4a4a;
  --white:#ffffff;
}
*{margin:0;padding:0;box-sizing:border-box}
html,body{width:1200px;height:3564px;overflow:hidden;background:var(--white)}
body{position:relative;font-family:'Poppins',sans-serif;color:var(--text)}
.abs{position:absolute}
svg.abs{display:block}
.logo{font-family:'Poppins',sans-serif;font-weight:500;color:var(--brown);display:flex;align-items:center;gap:10px;white-space:nowrap}
.logo .dot{width:14px;height:14px;border-radius:50%;background:var(--green)}
.nav{left:553px;top:82px;display:flex;gap:37px;font-size:15px;color:#222}
.nav .active{color:var(--green);font-weight:600}
.topbar{top:14px;left:740px;display:flex;align-items:center;gap:14px;font-size:19px}
.topbar .ico{width:34px;height:34px;border-radius:50%;display:flex;align-items:center;justify-content:center}
.phone{color:var(--green)}
.cart{color:#222}
.media{border-radius:8px}
.hero-title{left:518px;top:240px;font-size:52px;font-weight:500;color:var(--brown);letter-spacing:.5px}
.hero-sub{left:520px;top:302px;font-size:23px;color:var(--green)}
.feature{width:146px;text-align:center;font-size:21px;line-height:26px;color:var(--brown)}
.feature .ring{width:86px;height:86px;border-radius:50%;margin:0 auto 14px;background:radial-gradient(circle at 40% 35%,#7cc64a,#3f8a1f);border:3px solid #4f9a2a;box-shadow:0 0 0 3px #fff inset;display:flex;align-items:center;justify-content:center}
.section-title{width:1200px;text-align:center;font-size:38px;font-weight:500;color:var(--brown)}
.section-title span{color:var(--green)}
.step{width:280px;text-align:center}
.step h3{font-size:28px;font-weight:500;color:var(--brown);margin-bottom:14px}
.step p{font-size:13.5px;line-height:22px;color:#555}
.badge{width:66px;height:66px;border-radius:50%;color:#fff;font-size:28px;font-weight:500;display:flex;align-items:center;justify-content:center;border:4px solid #fff;box-shadow:0 2px 8px rgba(0,0,0,.25)}
.about-text{left:111px;top:1460px;width:500px;color:#fff}
.about-text h2{font-size:36px;font-weight:500;margin-bottom:60px}
.about-text p{font-size:14px;line-height:26px;margin-bottom:10px}
.btn-outline{display:inline-block;margin-top:24px;padding:11px 17px;border:2px solid #fff;border-radius:24px;font-size:14px;color:#fff}
.offer{left:752px;top:1478px;width:334px;height:334px;border-radius:50%;border:6px solid #fff;background:radial-gradient(circle at 50% 30%,#5aa52c,#2f7a12 70%);color:#fff;text-align:center}
.offer .upto{font-family:'Alice',serif;font-size:20px;margin-top:42px}
.offer .pct{font-family:'Alice',serif;font-size:48px;margin-top:6px}
.offer .tag{font-family:'Kaushan Script',cursive;font-size:30px;line-height:42px;margin-top:12px}
.product{width:300px;text-align:center}
.product .tile{height:125px;border-radius:4px}
.product h4{font-size:22px;font-weight:500;color:var(--brown);margin-top:24px}
.btn-green{display:inline-block;margin-top:18px;padding:12px 17px;border-radius:24px;background:var(--green);color:#fff;font-size:14px}
.arrow-btn{width:52px;height:52px;border-radius:50%;border:2px solid var(--brown);display:flex;align-items:center;justify-content:center}
.card{width:418px;height:232px;border:3px solid #fff;border-radius:6px;color:#fff;font-size:14px;line-height:20px}
.card h5{font-size:19px;font-weight:500;margin:112px 0 12px}
.avatar{width:132px;height:132px;border-radius:50%;border:4px solid #fff}
.quote{font-family:'Alice',serif;font-size:96px;line-height:1;color:#fff}
.foot-h{font-size:24px;font-weight:500;color:var(--brown)}
.links{list-style:none;font-size:17px;color:#333}
.links li{height:28px}
.links li::before{content:"›";margin-right:14px;color:#333}
.contact-row{display:flex;gap:12px;align-items:flex-start;font-size:15px;line-height:24px;color:#333}
.contact-row .c-ico{flex:none;width:44px;height:44px;border-radius:50%;border:2px solid var(--brown);display:flex;align-items:center;justify-content:center}
.pay{width:32px;height:20px;border-radius:3px;border:1px solid #ddd;background:#f3f3f3}
.copy{width:1200px;text-align:center;top:3519px;font-size:15px;color:#333}
</style>
</head>
<body>

<!-- Header -->
<svg class="abs" style="left:0;top:0" width="1200" height="190" viewBox="0 0 1200 190">
  <defs>
    <linearGradient id="hdrLine" x1="0" x2="1">
      <stop offset="0" stop-color="#5a2410"/><stop offset=".55" stop-color="#5a2410"/><stop offset=".8" stop-color="#6ab43e"/><stop offset="1" stop-color="#6ab43e"/>
    </linearGradient>
  </defs>
  <path d="M0 0H1200V102C1080 160 920 186 780 178C620 170 520 110 300 112C170 114 70 140 0 156Z" fill="#fdf2ee"/>
  <path d="M0 156C70 140 170 114 300 112C520 110 620 170 780 178C920 186 1080 160 1200 102" fill="none" stroke="url(#hdrLine)" stroke-width="4"/>
</svg>
<div class="abs logo" style="left:111px;top:32px;font-size:40px"><span class="dot"></span>Turf Tails</div>
<div class="abs topbar">
  <span class="ico" style="background:var(--green)"><svg width="16" height="16" viewBox="0 0 24 24"><path d="M6.6 10.8a15 15 0 006.6 6.6l2.2-2.2a1 1 0 011-.25 11.4 11.4 0 003.6.57 1 1 0 011 1V20a1 1 0 01-1 1A17 17 0 013 4a1 1 0 011-1h3.5a1 1 0 011 1c0 1.25.2 2.45.57 3.57a1 1 0 01-.25 1z" fill="#fff"/></svg></span>
  <span class="phone">+100 555 0142</span>
  <span class="ico" style="background:var(--brown)"><svg width="16" height="16" viewBox="0 0 24 24"><path d="M5 8h14l-1 13H6z" fill="none" stroke="#fff" stroke-width="2"/><path d="M9 8V6a3 3 0 016 0v2" fill="none" stroke="#fff" stroke-width="2"/></svg></span>
  <span class="cart">Cart: 0 Items</span>
</div>
<nav class="abs nav">
  <span class="active">HOME</span><span>ABOUT</span><span>MEDIA</span><span>PRODUCTS</span><span>FAQ</span><span>CONTACT</span>
</nav>

<!-- Hero -->
<div class="abs" role="img" aria-label="Strip of lush green grass along the bottom of the hero" style="left:0;top:545px;width:1200px;height:100px;background:linear-gradient(180deg,#9fd26a 0%,#6db23a 45%,#3f8a1f 100%)"></div>
<div class="abs media" role="img" aria-label="Fluffy tan puppy sitting in the grass" style="left:40px;top:195px;width:420px;height:450px;background:linear-gradient(180deg,#d8b98e 0%,#c39a68 55%,#a97d4d 100%)"></div>
<div class="abs hero-title">Turf Tails</div>
<div class="abs hero-sub">From our farm to your home</div>
<div class="abs feature" style="left:489px;top:365px"><div class="ring"><svg width="44" height="34" viewBox="0 0 44 34"><path d="M22 32V6M22 32L10 10M22 32L34 10M22 32L4 20M22 32L40 20" stroke="#fff" stroke-width="3" fill="none" stroke-linecap="round"/></svg></div>Natural<br>Grass</div>
<div class="abs feature" style="left:635px;top:365px"><div class="ring"><svg width="36" height="40" viewBox="0 0 36 40"><path d="M6 12h24l-3 26H9z M4 8h28" stroke="#fff" stroke-width="3" fill="none" stroke-linejoin="round"/></svg></div>Odor<br>Control</div>
<div class="abs feature" style="left:781px;top:365px"><div class="ring"><svg width="40" height="36" viewBox="0 0 40 36"><rect x="4" y="14" width="32" height="18" rx="3" stroke="#fff" stroke-width="3" fill="none"/><path d="M20 2c3 4 4 6 4 8a4 4 0 01-8 0c0-2 1-4 4-8z" fill="#fff"/></svg></div>Natural<br>Absorption</div>
<div class="abs feature" style="left:927px;top:365px"><div class="ring"><svg width="46" height="30" viewBox="0 0 46 30"><rect x="3" y="14" width="40" height="12" stroke="#fff" stroke-width="3" fill="none"/><path d="M6 14l3-8 3 8 3-8 3 8 3-8 3 8 3-8 3 8 3-8 3 8 3-8 3 8" stroke="#fff" stroke-width="2" fill="none"/></svg></div>Interlocking<br>Trays</div>

<!-- How it works -->
<div class="abs section-title" style="top:726px">How <span>It Works</span></div>

<div class="abs media" role="img" aria-label="Grass-plant character pointing at a mobile phone" style="left:95px;top:870px;width:250px;height:225px;background:linear-gradient(160deg,#eef6e6 0%,#a9d77c 100%)"></div>
<div class="abs media" role="img" aria-label="Grass-plant character stepping out of a cardboard delivery box" style="left:455px;top:870px;width:250px;height:225px;background:linear-gradient(160deg,#eef6e6 0%,#d9c29c 100%)"></div>
<div class="abs media" role="img" aria-label="Grass-plant character walking beside a grass tray" style="left:830px;top:890px;width:270px;height:205px;background:linear-gradient(160deg,#eef6e6 0%,#b7c9a8 100%)"></div>

<svg class="abs" style="left:0;top:850px" width="1200" height="300" viewBox="0 0 1200 300">
  <defs><marker id="ah" markerWidth="10" markerHeight="10" refX="6" refY="5" orient="auto"><path d="M0 0L10 5L0 10z" fill="#222"/></marker></defs>
  <path d="M365 30C410 -6 480 10 512 62" fill="none" stroke="#222" stroke-width="2" stroke-dasharray="4 4" marker-end="url(#ah)"/>
  <path d="M705 270C760 292 810 270 846 236" fill="none" stroke="#222" stroke-width="2" stroke-dasharray="4 4" marker-end="url(#ah)"/>
</svg>
<div class="abs badge" style="left:302px;top:873px;background:var(--brown)">01</div>
<div class="abs badge" style="left:654px;top:1049px;background:var(--green)">02</div>
<div class="abs badge" style="left:989px;top:890px;background:var(--brown)">03</div>

<div class="abs step" style="left:75px;top:1128px"><h3>1.Order</h3><p>Nemo enim ipsam voluptatem<br>quia voluptas sit aspernatur aut<br>odit aut fugit.</p></div>
<div class="abs step" style="left:441px;top:1128px"><h3>2.Open</h3><p>Nemo enim ipsam voluptatem<br>quia voluptas sit aspernatur aut<br>odit aut fugit.</p></div>
<div class="abs step" style="left:830px;top:1128px"><h3>3.Go</h3><p>Nemo enim ipsam voluptatem<br>quia voluptas sit aspernatur aut<br>odit aut fugit.</p></div>

<!-- About band -->
<svg class="abs" style="left:0;top:1315px" width="1200" height="640" viewBox="0 0 1200 640" role="img" aria-label="Terrier dog leaping beside a hay bale in a sunny green field">
  <defs>
    <linearGradient id="aboutBg" x1="0" x2="1">
      <stop offset="0" stop-color="#4a1c08"/><stop offset=".38" stop-color="#5e3410"/><stop offset=".6" stop-color="#6f8f2a"/><stop offset="1" stop-color="#8cc23c"/>
    </linearGradient>
  </defs>
  <path d="M0 62C90 20 150 0 230 8C340 18 420 72 540 74C680 76 760 30 860 22C960 14 1060 44 1200 54V570C1130 600 1060 620 980 612C880 600 820 566 700 570C560 574 460 636 330 636C200 636 100 590 0 560Z" fill="url(#aboutBg)"/>
</svg>
<div class="abs about-text">
  <h2>About Turf Tails</h2>
  <p>Nemo enim ipsam voluptatem quia voluptas sit aspernatur aut odit aut fugit, sed quia consequuntur magni dolores eos qui ratione voluptatem sequi nesciunt. Neque porro quisquam est, qui dolorem ipsum quia dolor sit amet, consectetur, adipisci velit.</p>
  <p>Magnam aliquam quaerat voluptatem. Ut enim ad minima veniam, quis nostrum exercitationem ullam corporis suscipit laboriosam, nisi ut aliquid ex ea commodi consequatur.</p>
  <span class="btn-outline">Read More</span>
</div>
<div class="abs offer">
  <div class="upto">UPTO</div>
  <div class="pct">25% OFF</div>
  <div class="tag">“Farm Fresh For<br>Your Furry<br>Friend!”</div>
</div>

<!-- Featured products -->
<div class="abs section-title" style="top:2014px">Featured <span>Product</span></div>
<div class="abs arrow-btn" style="left:28px;top:2226px"><svg width="18" height="24" viewBox="0 0 18 24"><path d="M14 2L4 12l10 10" fill="none" stroke="var(--brown)" stroke-width="2.5"/></svg></div>
<div class="abs arrow-btn" style="left:1118px;top:2226px"><svg width="18" height="24" viewBox="0 0 18 24"><path d="M4 2l10 10L4 22" fill="none" stroke="var(--brown)" stroke-width="2.5"/></svg></div>
<div class="abs product" style="left:110px;top:2152px"><div class="tile" role="img" aria-label="Square slab of lush turf with soil base" style="background:linear-gradient(180deg,#9ccf5a 0%,#5a9a26 70%,#6b3a1a 72%,#4e2a12 100%)"></div><h4>Meadow Plush™</h4><span class="btn-green">Read More</span></div>
<div class="abs product" style="left:450px;top:2152px"><div class="tile" role="img" aria-label="Square slab of bright green turf" style="background:linear-gradient(180deg,#a6d96a 0%,#4fa22a 78%,#5a4a3a 80%,#3a3028 100%)"></div><h4>Dewline™</h4><span class="btn-green">Read More</span></div>
<div class="abs product" style="left:792px;top:2152px"><div class="tile" role="img" aria-label="Square slab of fine-bladed green turf" style="background:linear-gradient(180deg,#8fcd5a 0%,#3f9a25 80%,#5d5d5d 82%,#3d3d3d 100%)"></div><h4>Verdant™</h4><span class="btn-green">Read More</span></div>

<!-- Testimonials band -->
<svg class="abs" style="left:0;top:2491px" width="1200" height="680" viewBox="0 0 1200 680" role="img" aria-label="Dog resting in tall green grass">
  <defs>
    <linearGradient id="testiBg" x1="0" y1="0" x2="0" y2="1">
      <stop offset="0" stop-color="#5aa02a"/><stop offset=".45" stop-color="#3e7a1c"/><stop offset="1" stop-color="#1f4a10"/>
    </linearGradient>
  </defs>
  <path d="M0 70C110 30 190 16 300 28C420 42 500 82 620 76C760 68 860 10 980 14C1080 18 1150 44 1200 62V600C1120 640 1020 660 900 640C780 620 700 580 560 586C430 592 360 680 230 672C140 666 60 630 0 610Z" fill="url(#testiBg)"/>
</svg>
<div class="abs section-title" style="top:2608px;color:#fff">Our Testimonials</div>

<div class="abs card" style="left:151px;top:2775px;text-align:right;padding:0 24px 0 14px">
  <h5>(Mark Ellison)</h5>
  <p>Nemo enim ipsam voluptatem quia voluptas sit asper natur aut odit aut fugit, sed quia consequuntur magni dolores eos qui ratione voluptatem.</p>
</div>
<div class="abs card" style="left:632px;top:2775px;padding:0 14px 0 22px">
  <h5>(Lena Moor)</h5>
  <p>Nemo enim ipsam voluptatem quia voluptas sit asper natur aut odit aut fugit, sed quia consequuntur magni dolores eos qui ratione .</p>
</div>
<div class="abs quote" style="left:394px;top:2805px">”</div>
<div class="abs quote" style="left:752px;top:2805px">“</div>
<div class="abs avatar" role="img" aria-label="Portrait of a customer" style="left:456px;top:2730px;background:linear-gradient(180deg,#d9bfa6,#9a7a60)"></div>
<div class="abs avatar" role="img" aria-label="Portrait of a customer" style="left:610px;top:2730px;background:linear-gradient(180deg,#dfc3ac,#7a553e)"></div>

<!-- Footer -->
<div class="abs logo" style="left:111px;top:3280px;font-size:46px"><span class="dot" style="width:18px;height:18px"></span>Turf Tails</div>
<div class="abs" style="left:111px;top:3394px;display:flex;gap:19px">
  <span class="pay"></span><span class="pay"></span><span class="pay"></span><span class="pay"></span><span class="pay"></span><span class="pay"></span>
</div>

<div class="abs foot-h" style="left:537px;top:3216px">Quick Links</div>
<ul class="abs links" style="left:537px;top:3264px">
  <li>HOME</li><li>ABOUT</li><li>MEDIA</li><li>PRODUCTS</li><li>FAQ</li><li>CONTACT</li>
</ul>

<div class="abs foot-h" style="left:795px;top:3216px">Contact Us</div>
<div class="abs contact-row" style="left:795px;top:3263px">
  <span class="c-ico"><svg width="18" height="22" viewBox="0 0 18 22"><path d="M9 21s7-7 7-12A7 7 0 002 9c0 5 7 12 7 12z" fill="none" stroke="var(--brown)" stroke-width="2"/><circle cx="9" cy="9" r="2.5" fill="none" stroke="var(--brown)" stroke-width="2"/></svg></span>
  <span style="font-size:14px">Address,<br>48 Meadow Lane, Fernbrook,<br>Northvale</span>
</div>
<div class="abs contact-row" style="left:795px;top:3348px">
  <span class="c-ico"><svg width="18" height="18" viewBox="0 0 24 24"><path d="M6.6 10.8a15 15 0 006.6 6.6l2.2-2.2a1 1 0 011-.25 11.4 11.4 0 003.6.57 1 1 0 011 1V20a1 1 0 01-1 1A17 17 0 013 4a1 1 0 011-1h3.5a1 1 0 011 1c0 1.25.2 2.45.57 3.57a1 1 0 01-.25 1z" fill="none" stroke="var(--brown)" stroke-width="2"/></svg></span>
  <span style="font-size:14px;padding-top:10px">Phone: +100 555 0142</span>
</div>
<div class="abs contact-row" style="left:795px;top:3404px">
  <span class="c-ico"><svg width="20" height="16" viewBox="0 0 20 16"><rect x="1" y="1" width="18" height="14" fill="none" stroke="var(--brown)" stroke-width="2"/><path d="M1 1l9 8 9-8" fill="none" stroke="var(--brown)" stroke-width="2"/></svg></span>
  <span style="font-size:14px;padding-top:10px">Email : hello@turftails.example</span>
</div>

<div class="abs" style="left:111px;top:3488px;width:978px;height:1px;background:#ccc"></div>
<div class="abs copy">Copyrights @ 2020 Turf Tails. All Rights Reserved.</div>

</body>
</html>
```